We need a brochure designed for the Brook Lodge, which is a holiday villa in Sri Lanka. The brochure will be sent to travel agents and holiday travellers by email and also be printed and placed at the Brook Lodge. The brochure should be sophisticated yet indicate a sense of adventure.

```html
<!DOCTYPE html>
<html lang="en">
<head>
<meta charset="utf-8">
<title>Brook Lodge Brochure Cover</title>
<link href="https://fonts.googleapis.com/css2?family=Open+Sans:wght@400;600&family=Tenor+Sans&display=swap" rel="stylesheet">
<style>
  :root {
    --backdrop: #b8d8d9;
    --paper: #f6f6f4;
    --teal: #1aa6b8;
    --teal-deep: #1d8a93;
    --frame-line: #a9b3b3;
    --frame-line-light: rgba(255,255,255,0.55);
    --photo-dark: #2f4a26;
    --photo-mid: #5d7a3a;
    --photo-stone: #8a7c66;
    --muted-text: #8a9596;
  }
  * { margin: 0; padding: 0; box-sizing: border-box; }
  html, body {
    width: 1200px;
    height: 700px;
    overflow: hidden;
    background: var(--backdrop);
  }
  .canvas {
    position: relative;
    width: 1200px;
    height: 700px;
  }
  .cover {
    position: absolute;
    left: 130px;
    top: 30px;
    width: 940px;
    height: 640px;
    background: var(--paper);
    box-shadow: 0 6px 18px rgba(40, 80, 80, 0.18);
  }
  .cover-photo {
    position: absolute;
    left: 22px;
    top: 22px;
    width: 600px;
    height: 596px;
    background:
      radial-gradient(ellipse at 45% 22%, #d9ded6 0%, rgba(217,222,214,0) 22%),
      radial-gradient(ellipse at 70% 70%, var(--photo-stone) 0%, rgba(138,124,102,0) 45%),
      radial-gradient(ellipse at 85% 45%, #7ea24a 0%, rgba(126,162,74,0) 40%),
      linear-gradient(160deg, var(--photo-dark) 0%, var(--photo-mid) 45%, #3f5e2a 100%);
  }
  .headline-frame {
    position: absolute;
    left: 230px;
    top: 270px;
    width: 350px;
    height: 130px;
    border: 1px solid var(--frame-line-light);
  }
  .headline {
    position: absolute;
    left: 262px;
    top: 298px;
    font-family: "Open Sans", sans-serif;
    font-weight: 400;
    font-size: 27px;
    line-height: 1.2;
    color: #ffffff;
  }
  .headline .accent { color: var(--teal); display: block; }
  .brand-frame {
    position: absolute;
    left: 500px;
    top: 160px;
    width: 340px;
    height: 130px;
    border: 1px solid var(--frame-line);
  }
  .brand-name {
    position: absolute;
    left: 650px;
    top: 206px;
    width: 180px;
    text-align: center;
    font-family: "Tenor Sans", sans-serif;
    font-size: 19px;
    letter-spacing: 2px;
    line-height: 1.35;
    color: var(--teal-deep);
  }
  .edge-tab {
    position: absolute;
    right: 0;
    top: 380px;
    width: 34px;
    height: 12px;
    background: var(--teal);
  }
  .web-address {
    position: absolute;
    right: 40px;
    bottom: 46px;
    display: flex;
    align-items: center;
    gap: 8px;
    font-family: "Open Sans", sans-serif;
    font-size: 12px;
    letter-spacing: 2.5px;
    color: var(--muted-text);
  }
  .web-address svg { width: 10px; height: 10px; }
</style>
</head>
<body>
<div class="canvas">
  <section class="cover">
    <div class="cover-photo" role="img" aria-label="Stone garden steps leading up through tropical plants to a white two-storey villa among tall trees"></div>
    <div class="brand-frame"></div>
    <div class="headline-frame"></div>
    <h1 class="headline"><span class="accent">Escape from the</span>demands of city life</h1>
    <div class="brand-name">THE BROOK LODGE</div>
    <div class="edge-tab"></div>
    <div class="web-address">
      <svg viewBox="0 0 10 10" aria-hidden="true"><circle cx="5" cy="5" r="4.5" fill="var(--teal)"/></svg>
      <span>www.brook-lodge.com</span>
    </div>
  </section>
</div>
</body>
</html>
```